Lanterns Over the Silent Harbor

This book cover must convey the fact that the scientific evidence is clear that the afterlife is a reality. Attached are two ideas, but they're not working for me as they are. It could be that I'm not a graphic artist and can't get the composition correct. If there is a view of the afterlife, it must be realistic. The afterlife is just like this life. We can't use the family photo. I don't have permission.

```html
<!DOCTYPE html>
<html lang="en">
<head>
<meta charset="utf-8">
<title>Lanterns Over the Silent Harbor — Book Cover</title>
<link rel="stylesheet" href="https://fonts.googleapis.com/css2?family=Cormorant+Garamond:wght@500;600&family=Lobster&family=Playfair+Display:wght@700&display=swap">
<style>
  :root {
    --sky-top: #e8e7ea;
    --sky-mid: #f5f1ec;
    --glow: #fffaf0;
    --haze: #fbeed8;
    --gold: #eab66a;
    --amber: #d0904a;
    --ground: #c89468;
    --path: #b38870;
    --tree: rgba(96, 58, 28, 0.78);
    --title: #7a4a3c;
    --ghost: rgba(200, 148, 138, 0.32);
    --ghost-soft: rgba(200, 148, 138, 0.2);
    --author: #ffffff;
  }
  * { margin: 0; padding: 0; box-sizing: border-box; }
  html, body { width: 848px; height: 1200px; overflow: hidden; background: var(--sky-top); }
  .cover {
    position: relative;
    width: 848px;
    height: 1200px;
    overflow: hidden;
  }
  .cover-photo {
    position: absolute;
    inset: 0;
    background:
      radial-gradient(ellipse 210px 150px at 430px 1160px, rgba(120, 84, 72, 0.55) 0%, rgba(120, 84, 72, 0) 100%),
      radial-gradient(ellipse 180px 120px at 150px 1040px, rgba(110, 80, 60, 0.35) 0%, rgba(110, 80, 60, 0) 100%),
      radial-gradient(ellipse 180px 120px at 720px 1040px, rgba(110, 80, 60, 0.35) 0%, rgba(110, 80, 60, 0) 100%),
      radial-gradient(ellipse 190px 300px at 60px 760px, var(--tree) 0%, rgba(96, 58, 28, 0) 100%),
      radial-gradient(ellipse 140px 200px at 250px 860px, rgba(150, 90, 40, 0.55) 0%, rgba(150, 90, 40, 0) 100%),
      radial-gradient(ellipse 340px 200px at 500px 690px, var(--glow) 0%, rgba(255, 250, 240, 0) 100%),
      linear-gradient(180deg, var(--sky-top) 0%, var(--sky-mid) 32%, var(--haze) 58%, var(--gold) 73%, var(--amber) 80%, var(--ground) 88%, var(--path) 100%);
  }
  .title-line {
    position: absolute;
    left: 0;
    right: 0;
    text-align: center;
    color: var(--title);
    line-height: 1;
    white-space: nowrap;
  }
  .title-kicker {
    top: 99px;
    font-family: "Cormorant Garamond", serif;
    font-weight: 600;
    font-size: 60px;
    letter-spacing: 3px;
  }
  .title-joiner {
    top: 162px;
    left: 12px;
    font-family: "Lobster", cursive;
    font-size: 56px;
  }
  .title-main {
    font-family: "Cormorant Garamond", serif;
    font-weight: 600;
    font-size: 180px;
    left: -18px;
  }
  .title-main-first { top: 211px; }
  .title-main-second { top: 347px; }
  .ghost-letter {
    position: absolute;
    font-family: "Cormorant Garamond", serif;
    font-weight: 500;
    color: var(--ghost);
    line-height: 1;
  }
  .ghost-left { left: 72px; top: 171px; font-size: 185px; }
  .ghost-right { left: 664px; top: 174px; font-size: 235px; }
  .ghost-low { left: 543px; top: 441px; font-size: 100px; color: var(--ghost-soft); }
  .author {
    position: absolute;
    left: 0;
    right: 0;
    top: 1076px;
    text-align: center;
    font-family: "Playfair Display", serif;
    font-weight: 700;
    font-size: 24px;
    line-height: 1;
    color: var(--author);
    padding-left: 8px;
  }
</style>
</head>
<body>
  <main class="cover">
    <div class="cover-photo" role="img" aria-label="Realistic sunset photograph of a quiet harbor path glowing with warm lantern light, figures walking hand in hand toward the bright horizon, bare trees on the left and golden fields ahead, suggesting an afterlife just like this life"></div>

    <span class="ghost-letter ghost-left" aria-hidden="true">S</span>
    <span class="ghost-letter ghost-right" aria-hidden="true">T</span>
    <span class="ghost-letter ghost-low" aria-hidden="true">R</span>

    <h1 class="title">
      <span class="title-line title-kicker">LANTERNS OVER</span>
      <span class="title-line title-joiner">the</span>
      <span class="title-line title-main title-main-first">SILENT</span>
      <span class="title-line title-main title-main-second">HARBOR</span>
    </h1>

    <p class="author">M. Ellis Varden, PhD</p>
  </main>
</body>
</html>
```